Business Cards

We were billed for this because the project timed out. Please give me another designed to open this back up. I was not happy with the last designs (that I was charged for).
we are also using the logo with Revitalizing Pools One Drop at a Time
Also want to utilize Where Healthy Water is our Commitment.

Contact Information for Business Card

Marlowe Stone Group Inc

```html
<!DOCTYPE html>
<html lang="en">
<head>
<meta charset="utf-8">
<title>Marlowe Stone Group Inc — Business Cards</title>
<link rel="stylesheet" href="https://fonts.googleapis.com/css2?family=Montserrat:wght@500;700;800&family=Arimo:wght@400;700&display=swap">
<style>
  :root {
    --backdrop: #2d2d2d;
    --card: #000000;
    --blue-light: #3fa1de;
    --blue-deep: #1a6fbe;
    --gray-mark: #4d4d4d;
    --gray-tag: #5a5a5a;
    --white: #ffffff;
  }
  * { box-sizing: border-box; margin: 0; padding: 0; }
  html, body {
    width: 1200px; height: 1015px; overflow: hidden;
    background: var(--backdrop);
  }
  .sheet {
    position: relative; width: 1200px; height: 1015px;
    display: flex; flex-direction: column; align-items: center; justify-content: center;
    gap: 48px;
  }
  .card {
    position: relative; width: 640px; height: 366px;
    background: var(--card);
    box-shadow: 0 10px 24px rgba(0,0,0,.45);
    overflow: hidden;
  }
  .card__stripe {
    position: absolute; left: 0; right: 0; bottom: 0; height: 9px;
    background: linear-gradient(90deg, var(--blue-light) 0 52%, var(--blue-deep) 52% 100%);
  }

  /* Front */
  .front__brand {
    position: absolute; left: 0; right: 0; top: 92px;
    display: flex; flex-direction: column; align-items: center;
  }
  .brand-row { display: flex; align-items: center; gap: 14px; }
  .brand-square { width: 30px; height: 30px; background: var(--blue-light); }
  .front__name {
    font-family: "Montserrat", sans-serif; font-weight: 800;
    font-size: 34px; letter-spacing: 2px; color: var(--gray-mark);
    text-transform: uppercase;
  }
  .front__tagline {
    margin-top: 10px;
    font-family: "Arimo", sans-serif; font-weight: 400;
    font-size: 14px; letter-spacing: 4.6px; color: var(--gray-tag);
    text-transform: uppercase;
  }
  .front__commitment {
    position: absolute; left: 0; right: 0; top: 250px; text-align: center;
    font-family: "Montserrat", sans-serif; font-weight: 700;
    font-size: 22px; color: var(--blue-light);
  }

  /* Back */
  .back__contact {
    position: absolute; left: 58px; top: 56px;
    font-family: "Arimo", sans-serif; color: var(--white);
  }
  .person__name {
    font-size: 25px; font-weight: 700; color: var(--blue-deep);
    text-transform: uppercase; letter-spacing: .3px;
  }
  .person__name span { color: var(--blue-light); }
  .person__role { font-size: 15px; text-transform: uppercase; margin-top: 2px; }
  .rule { width: 150px; height: 1px; background: var(--blue-light); margin: 16px 0 14px; }
  .contact-list { list-style: none; font-size: 18px; line-height: 26px; }
  .contact-list li { display: flex; align-items: center; gap: 10px; }
  .contact-list svg { width: 17px; height: 17px; flex: none; }
  .address { font-size: 18px; line-height: 24px; }

  .back__brand {
    position: absolute; right: 42px; top: 72px;
    display: flex; align-items: center; gap: 12px;
  }
  .back__brand .brand-square { width: 34px; height: 34px; }
  .back__name {
    font-family: "Montserrat", sans-serif; font-weight: 800;
    font-size: 30px; line-height: 1.05; color: var(--blue-light);
    text-transform: uppercase; letter-spacing: 1px;
  }
</style>
</head>
<body>
<main class="sheet">

  <section class="card card--front" aria-label="Business card front">
    <div class="front__brand">
      <div class="brand-row">
        <span class="brand-square"></span>
        <span class="front__name">Marlowe Stone Group</span>
      </div>
      <p class="front__tagline">Revitalizing Pools One Drop at a Time</p>
    </div>
    <p class="front__commitment">Where Healthy Water is Our Commitment</p>
    <div class="card__stripe"></div>
  </section>

  <section class="card card--back" aria-label="Business card back">
    <div class="back__contact">
      <p class="person__name">Elias <span>Ward</span></p>
      <p class="person__role">Managing Director</p>
      <div class="rule"></div>
      <ul class="contact-list">
        <li>
          <svg viewBox="0 0 24 24" aria-hidden="true"><path fill="#1a6fbe" d="M6.6 10.8a15 15 0 0 0 6.6 6.6l2.2-2.2c.3-.3.7-.4 1-.2 1.1.4 2.3.6 3.6.6.6 0 1 .4 1 1V20c0 .6-.4 1-1 1A17 17 0 0 1 3 4c0-.6.4-1 1-1h3.5c.6 0 1 .4 1 1 0 1.3.2 2.5.6 3.6.1.3 0 .7-.2 1z"/></svg>
          044-123 456 789
        </li>
        <li>
          <svg viewBox="0 0 24 24" aria-hidden="true"><rect x="2" y="5" width="20" height="14" fill="#1a6fbe"/><path d="M2 5l10 8 10-8" fill="none" stroke="#000" stroke-width="1.6"/></svg>
          info@webname.com
        </li>
        <li>
          <svg viewBox="0 0 24 24" aria-hidden="true"><g fill="none" stroke="#1a6fbe" stroke-width="2"><circle cx="12" cy="12" r="9"/><ellipse cx="12" cy="12" rx="4" ry="9"/><path d="M3 12h18M5 7h14M5 17h14"/></g></svg>
          www.websitename.com
        </li>
      </ul>
      <div class="rule"></div>
      <p class="address">421, Address line goes here<br>45452, Country Name</p>
    </div>

    <div class="back__brand">
      <span class="brand-square"></span>
      <span class="back__name">Marlowe<br>Stone Group</span>
    </div>
    <div class="card__stripe"></div>
  </section>

</main>
</body>
</html>
```